Custom Monogramming and Retail gifts

We need a Business Card for a monogramming business that offers many retail gift options. We are a home based business that uses social media (Chatterbox,clipboardia and our website) to sell our products. Our target market is college age, high school, baby gifts.
We want a preppy fun look. Monogramming is very popular in the South

Industry/Entity Type

College

Contact Information for Business Card

Threadwell Keepsakes
Custom Monogramming and Gifts
7152 Brackenway Lane
Gainesville, GA 30999
Della Marsh, Owner
555-314-2790
threadwellkeepsakes.example
threadwellkeepsakes@mailbox.example

```html
<!DOCTYPE html>
<html lang="en">
<head>
<meta charset="utf-8">
<title>Threadwell Keepsakes – Business Card Options</title>
<link rel="stylesheet" href="https://fonts.googleapis.com/css2?family=Tinos:wght@700&family=Comic+Neue:wght@700&family=Patrick+Hand&display=swap">
<style>
  :root {
    --board: #1d1d1d;
    --card: #ffffff;
    --ink: #111111;
    --pink: #e4407a;
    --check: #f4b3c7;
    --check-deep: #ee8fae;
    --rule: #111111;
  }
  * { box-sizing: border-box; margin: 0; padding: 0; }
  html, body { width: 800px; height: 1200px; overflow: hidden; }
  body { background: var(--board); position: relative; }

  .card {
    position: absolute;
    background: var(--card);
    box-shadow: 0 6px 18px rgba(0,0,0,.55);
    overflow: hidden;
  }
  .card--classic { left: 43px; top: 103px; width: 716px; height: 418px; }
  .card--script  { left: 43px; top: 647px; width: 724px; height: 424px; }

  .card__pattern {
    position: absolute; left: 0; top: 0; bottom: 0;
    background: linear-gradient(135deg, var(--check) 0%, var(--check-deep) 50%, var(--check) 100%);
    opacity: .75;
  }
  .card--classic .card__pattern { width: 174px; }
  .card--script .card__pattern { width: 176px; }

  .card__divider {
    position: absolute; top: 0; bottom: 0; width: 4px; background: var(--rule);
  }
  .card--classic .card__divider { left: 174px; }
  .card--script .card__divider { left: 176px; }

  .badge {
    position: absolute;
    border-radius: 50%;
    background: var(--card);
    border: 5px solid var(--rule);
    display: flex; flex-direction: column; align-items: center; justify-content: center;
    text-align: center;
    font-family: "Tinos", serif; font-weight: 700; color: var(--pink);
    box-shadow: 0 2px 6px rgba(0,0,0,.25);
  }
  .card--classic .badge { left: 36px; top: 100px; width: 212px; height: 212px; }
  .card--script .badge { left: 37px; top: 91px; width: 220px; height: 220px; }
  .badge__name { font-size: 27px; line-height: 1.1; }
  .badge__site { font-size: 11px; margin-top: 16px; }

  .details { position: absolute; color: var(--ink); }
  .card--classic .details { left: 351px; top: 79px; }
  .card--script .details { left: 347px; top: 73px; }

  .details__name {
    font-family: "Tinos", serif; font-weight: 700; font-size: 26px; line-height: 32px;
    color: var(--pink); white-space: nowrap;
  }
  .card--script .details__name { font-size: 27px; color: var(--ink); }
  .details__name .accent { color: var(--pink); }
  .details__tagline {
    font-family: "Tinos", serif; font-weight: 700; font-size: 19px; line-height: 26px;
    white-space: nowrap; margin-top: 6px;
  }
  .card--script .details__tagline { margin-top: 3px; }

  .contact { list-style: none; }
  .contact__item { display: flex; align-items: flex-start; white-space: nowrap; }
  .contact__icon { width: 24px; height: 18px; margin-right: 13px; flex: none; }
  .contact__text { display: block; }

  .card--classic .contact { font-family: "Comic Neue", sans-serif; font-weight: 700; font-size: 16px; line-height: 31px; margin-top: 32px; }
  .card--classic .contact__item + .contact__item { margin-top: 6px; }
  .card--classic .contact__icon { color: var(--ink); margin-top: 6px; }

  .card--script .contact { font-family: "Patrick Hand", cursive; font-size: 20px; line-height: 32px; color: var(--pink); margin-top: 48px; }
  .card--script .contact__item + .contact__item { margin-top: 3px; }
  .card--script .contact__icon { color: var(--pink); margin-top: 7px; }
</style>
</head>
<body>

<section class="card card--classic" aria-label="Business card, classic type">
  <div class="card__pattern" role="img" aria-label="Pink gingham check pattern panel"></div>
  <div class="card__divider"></div>
  <div class="badge">
    <span class="badge__name">Threadwell<br>Keepsakes</span>
    <span class="badge__site">threadwellkeepsakes.example</span>
  </div>
  <div class="details">
    <h1 class="details__name">Threadwell Keepsakes</h1>
    <p class="details__tagline">Custom Monogramming and Gifts</p>
    <ul class="contact">
      <li class="contact__item">
        <svg class="contact__icon" viewBox="0 0 24 18"><path d="M0 3 L24 9 L0 15 L6 9 Z" fill="currentColor"/></svg>
        <span class="contact__text">7152 Brackenway<br>Lane Gainesville, GA 30999<br>Della Marsh, Owner</span>
      </li>
      <li class="contact__item">
        <svg class="contact__icon" viewBox="0 0 24 18"><path d="M2 7 Q12 0 22 7 L19 9 L16 6 L8 6 L5 9 Z M6 9 L18 9 L20 17 L4 17 Z" fill="currentColor"/><circle cx="12" cy="13" r="2.4" fill="#fff"/></svg>
        <span class="contact__text">555-314-2790</span>
      </li>
      <li class="contact__item">
        <svg class="contact__icon" viewBox="0 0 24 18"><rect x="2" y="3" width="20" height="13" fill="none" stroke="currentColor" stroke-width="1.5"/><path d="M2 3 L12 11 L22 3 M2 16 L9 9 M22 16 L15 9" fill="none" stroke="currentColor" stroke-width="1.5"/></svg>
        <span class="contact__text">threadwellkeepsakes@mailbox.example</span>
      </li>
    </ul>
  </div>
</section>

<section class="card card--script" aria-label="Business card, script type">
  <div class="card__pattern" role="img" aria-label="Pink gingham check pattern panel"></div>
  <div class="card__divider"></div>
  <div class="badge">
    <span class="badge__name">Threadwell<br>Keepsakes</span>
    <span class="badge__site">threadwellkeepsakes.example</span>
  </div>
  <div class="details">
    <h2 class="details__name">Threadwell <span class="accent">Keepsakes</span></h2>
    <p class="details__tagline">Custom Monogramming and Gifts</p>
    <ul class="contact">
      <li class="contact__item">
        <svg class="contact__icon" viewBox="0 0 24 18"><path d="M0 3 L24 9 L0 15 L6 9 Z" fill="currentColor"/></svg>
        <span class="contact__text">7152 Brackenway<br>Lane Gainesville, GA 30999<br>Della Marsh, Owner</span>
      </li>
      <li class="contact__item">
        <svg class="contact__icon" viewBox="0 0 24 18"><path d="M2 7 Q12 0 22 7 L19 9 L16 6 L8 6 L5 9 Z M6 9 L18 9 L20 17 L4 17 Z" fill="currentColor"/><circle cx="12" cy="13" r="2.4" fill="#fff"/></svg>
        <span class="contact__text">555-314-2790</span>
      </li>
      <li class="contact__item">
        <svg class="contact__icon" viewBox="0 0 24 18"><rect x="2" y="3" width="20" height="13" fill="none" stroke="currentColor" stroke-width="1.5"/><path d="M2 3 L12 11 L22 3 M2 16 L9 9 M22 16 L15 9" fill="none" stroke="currentColor" stroke-width="1.5"/></svg>
        <span class="contact__text">threadwellkeepsakes@mailbox.example</span>
      </li>
    </ul>
  </div>
</section>

</body>
</html>
```